Fresh Produce Outlet needs a Poster Design

Hi,
We are Brightleaf Harvest Market, a fruit and veg outlet based in the suburb of Yanchep, Perth, Western Australia.Apart from fresh produce, we also stock nuts and grains, organic products and specialty grocery. We are about to launch a re-branding exercise, projecting ourselves as 'the' shop for fresh produce; quality, taste and freshness being our key differentiators. We are competing against a big supermarket chain who are using marketing muscle power to shut us down and we want to respond with a series of posters which are simple yet bold and sends a clear and positive message to our customers about what we have to offer.
Please feel free to visit our Facebook page www.facebook.com/brightleafharvestmkt to get an idea about our current branding,logo and the shop in general.
Regards
Team - Brightleaf Harvest Market
Target Market(s)
Residents of Yanchep and surrounding suburbs
Industry/Entity Type
Retail
Look and feel

```html
<!DOCTYPE html>
<html lang="en">
<head>
<meta charset="utf-8">
<title>Brightleaf Harvest Market – Posters</title>
<link href="https://fonts.googleapis.com/css2?family=Oswald:wght@500;700&display=swap" rel="stylesheet">
<style>
  :root {
    --ink: #3d3d3d;
    --green: #5cbc2a;
    --green-deep: #1f9a2f;
    --green-light: #8fd14f;
    --coral: #f0584f;
    --white: #ffffff;
  }
  html, body { margin: 0; padding: 0; overflow: hidden; background: var(--white); }
  .canvas {
    width: 880px; height: 1200px; position: relative; overflow: hidden;
    font-family: "Oswald", "Arial Narrow", sans-serif;
  }
  .poster { position: relative; width: 880px; height: 600px; overflow: hidden; background: var(--white); }
  .headline {
    position: absolute; left: 18px; top: 14px; margin: 0;
    font-weight: 700; font-size: 46px; line-height: 40px; text-transform: uppercase;
    color: var(--ink); letter-spacing: -0.5px;
  }
  .headline .accent { color: var(--green); }
  .cta {
    position: absolute; left: 18px; top: 298px; margin: 0;
    font-weight: 700; font-size: 58px; line-height: 60px; color: var(--coral);
  }
  .produce-photo {
    position: absolute; left: 300px; top: 14px; width: 566px; height: 320px;
    border-radius: 40% 40% 30% 30% / 50% 50% 40% 40%;
  }
  .produce-photo.vegetables {
    background: radial-gradient(ellipse at 50% 50%, #8cc152 0%, #d9493b 45%, #f4efe6 75%, rgba(255,255,255,0) 100%);
  }
  .produce-photo.fruits {
    background: radial-gradient(ellipse at 50% 55%, #f7c64a 0%, #f08a2c 35%, #d64436 55%, #f6efe2 78%, rgba(255,255,255,0) 100%);
  }
  .band { position: absolute; left: 0; top: 340px; width: 880px; height: 260px; }
  .brand {
    position: absolute; left: 18px; top: 430px; display: flex; align-items: center; gap: 16px;
  }
  .brand-name {
    margin: 0; color: var(--white); font-weight: 700; font-size: 44px; line-height: 44px;
    text-transform: uppercase;
  }
  .brand-dot { width: 34px; height: 34px; border-radius: 50%; background: var(--white); }
  .tagline {
    position: absolute; right: 28px; top: 512px; margin: 0; color: var(--white);
    font-weight: 500; font-size: 21px; line-height: 24px; text-transform: uppercase; letter-spacing: 0.5px;
  }
</style>
</head>
<body>
<div class="canvas">

  <section class="poster">
    <h1 class="headline">Do you<br>need<br><span class="accent">the fresh<br>vegetables</span><br>for the<br><span class="accent">best price</span><br>around?</h1>
    <p class="cta">VISIT US!</p>
    <div class="produce-photo vegetables" role="img" aria-label="Photo of fresh vegetables: cabbage, cauliflower, red peppers, chillies, onions and garlic"></div>
    <svg class="band" viewBox="0 0 880 260" aria-hidden="true">
      <path d="M0 40 C250 -10 560 -20 880 30 L880 260 L0 260 Z" fill="var(--green-light)"/>
      <path d="M0 60 C260 10 560 0 880 55 L880 260 L0 260 Z" fill="var(--green-deep)"/>
      <path d="M0 60 C300 20 600 30 880 90 L880 110 C600 60 300 55 0 85 Z" fill="var(--green)" opacity="0.8"/>
    </svg>
    <div class="brand">
      <p class="brand-name">Brightleaf<br>Harvest<br>Market</p>
      <span class="brand-dot"></span>
    </div>
    <p class="tagline">The quality<br>you deserve.</p>
  </section>

  <section class="poster">
    <h1 class="headline">Do you<br>need<br><span class="accent">the fresh<br>fruits</span><br>for the<br><span class="accent">best price</span><br>around?</h1>
    <p class="cta" style="top:298px">VISIT US!</p>
    <div class="produce-photo fruits" role="img" aria-label="Photo of fresh fruits: bananas, oranges, apples, kiwi, grapefruit and persimmons"></div>
    <svg class="band" viewBox="0 0 880 260" aria-hidden="true">
      <path d="M0 40 C250 -10 560 -20 880 30 L880 260 L0 260 Z" fill="var(--green-light)"/>
      <path d="M0 60 C260 10 560 0 880 55 L880 260 L0 260 Z" fill="var(--green-deep)"/>
      <path d="M0 60 C300 20 600 30 880 90 L880 110 C600 60 300 55 0 85 Z" fill="var(--green)" opacity="0.8"/>
    </svg>
    <div class="brand">
      <p class="brand-name">Brightleaf<br>Harvest<br>Market</p>
      <span class="brand-dot"></span>
    </div>
    <p class="tagline">The quality<br>you deserve.</p>
  </section>

</div>
</body>
</html>
```